Personal Training card design

i am a enthusiastic personal trainer wanting to appeal to as many people as possible.

offering health screening, single or group personal training, geared towards helping the client achieve their goal no matter what it is.

providing a professional service in a top gym facility.

I want to come across professional and trustworthy.

I want my card to be timeless and not look out of date in a years time.

I want the card to be informative and clear about what I offer and display my contact details.

ideally id like the colours blue and white but open to other colour options.

I want the final outcome to communicate professionalism, a PT the clients can trust, and that I can do what I claim.

id like a logo similar to the picture I have provided (the logo on the left hand side) if possible incorporating my initials "CD" or "CDT" but not essential.

Industry/Entity Type

Professional Service

Contact Information for Business Card

CalumDarbyTraining

"Real Results For Every Body"

specializing in
- weight loss & tone
- strength and conditioning
- nutritional advice

Book your free consultation today and take the first step toward achieving your goal!

for details contact me via
email: calumdarbytraining.co.uk
phone: 07700918342

or..
visit me via
facebook: calumdarbytraining
twitter: @calumdarbytraining

```html
<!DOCTYPE html>
<html lang="en">
<head>
<meta charset="utf-8">
<title>Calum Darby Training – Business Card Design Ideas</title>
<link rel="stylesheet" href="https://fonts.googleapis.com/css2?family=Mulish:wght@300;400;600;700;800&display=swap">
<style>
  :root {
    --board: #757679;
    --brand-blue: #3d66b0;
    --card-light: #edefee;
    --slate: #858384;
    --ink: #4a4a4c;
    --ink-grey: #7a7a7c;
    --white: #ffffff;
    --shadow: 0 8px 14px rgba(0,0,0,0.28);
  }
  * { box-sizing: border-box; margin: 0; padding: 0; }
  html, body { width: 1200px; height: 900px; overflow: hidden; }
  body {
    background: var(--board);
    font-family: "Mulish", sans-serif;
    position: relative;
  }
  .board-title {
    position: absolute; left: 198px; top: 70px;
    font-weight: 300; font-size: 31px; color: var(--white);
    letter-spacing: 0.2px;
  }
  .card {
    position: absolute; width: 365px; height: 250px;
    box-shadow: var(--shadow); overflow: hidden;
  }
  .card--front-blue { left: 200px; top: 200px; background: var(--brand-blue); }
  .card--front-light { left: 670px; top: 200px; background: var(--card-light); }
  .card--back-blue { left: 198px; top: 498px; background: var(--card-light); }
  .card--back-slate { left: 671px; top: 498px; background: var(--card-light); height: 252px; }

  /* front lockup */
  .lockup {
    position: absolute; left: 30px; top: 78px;
    display: flex; align-items: center; gap: 18px;
  }
  .lockup__dot { width: 64px; height: 64px; border-radius: 50%; flex: none; }
  .lockup__name { font-weight: 800; line-height: 1; }
  .lockup__first { display: block; font-size: 26px; }
  .lockup__second { display: block; font-size: 40px; margin-top: 4px; letter-spacing: 0.5px; }
  .lockup__tagline { display: block; font-weight: 700; font-size: 13px; margin-top: 8px; }

  .card--front-blue .lockup__dot { background: var(--white); }
  .card--front-blue .lockup__name { color: var(--white); }
  .card--front-blue .lockup__tagline { color: #d6dcf0; }
  .card--front-light .lockup__dot { background: var(--brand-blue); }
  .card--front-light .lockup__name { color: var(--brand-blue); }
  .card--front-light .lockup__tagline { color: var(--ink-grey); }

  /* back */
  .back-header {
    height: 103px; position: relative; color: var(--white);
  }
  .card--back-blue .back-header { background: var(--brand-blue); }
  .card--back-slate .back-header { background: var(--slate); }
  .back-header__brand { position: absolute; left: 30px; top: 24px; }
  .back-header__name { font-weight: 800; line-height: 1; color: var(--white); }
  .back-header__first { display: block; font-size: 16px; }
  .back-header__second { display: block; font-size: 21px; margin-top: 3px; letter-spacing: 0.4px; }
  .back-header__intro { display: block; font-size: 11px; margin-top: 3px; }

  .services { position: absolute; left: 183px; top: 25px; list-style: none; }
  .services li {
    display: flex; align-items: center; gap: 9px;
    font-size: 11px; height: 21px;
  }
  .services li::before {
    content: ""; width: 10px; height: 10px; border-radius: 50%;
    background: var(--white); flex: none;
  }

  .back-body { position: relative; height: 147px; }
  .invite {
    position: absolute; left: 30px; top: 36px; width: 132px;
    font-size: 11px; line-height: 12.6px; color: var(--ink);
  }
  .contacts { position: absolute; left: 182px; top: 39px; list-style: none; }
  .contacts li {
    display: flex; align-items: center; gap: 8px;
    font-size: 12px; height: 20px; color: var(--ink);
  }
  .contact-icon {
    width: 15px; height: 15px; border-radius: 50%; background: var(--brand-blue);
    flex: none; display: flex; align-items: center; justify-content: center;
    color: var(--white); font-size: 10px; font-weight: 700; line-height: 1;
  }
  .contact-icon svg { width: 9px; height: 9px; }
</style>
</head>
<body>
  <h1 class="board-title">Buisness Card Design Ideas</h1>

  <section class="card card--front-blue" aria-label="Front, blue">
    <div class="lockup">
      <span class="lockup__dot"></span>
      <div>
        <p class="lockup__name"><span class="lockup__first">Calum Darby</span><span class="lockup__second">TRAINING</span></p>
        <span class="lockup__tagline">Real Results For Every Body</span>
      </div>
    </div>
  </section>

  <section class="card card--front-light" aria-label="Front, light">
    <div class="lockup">
      <span class="lockup__dot"></span>
      <div>
        <p class="lockup__name"><span class="lockup__first">Calum Darby</span><span class="lockup__second">TRAINING</span></p>
        <span class="lockup__tagline">Real Results For Every Body</span>
      </div>
    </div>
  </section>

  <section class="card card--back-blue" aria-label="Back, blue">
    <div class="back-header">
      <div class="back-header__brand">
        <p class="back-header__name"><span class="back-header__first">Calum Darby</span><span class="back-header__second">TRAINING</span></p>
        <span class="back-header__intro">Specializing in ...</span>
      </div>
      <ul class="services">
        <li>Weight loss &amp; tone</li>
        <li>Strength and conditioning</li>
        <li>Nutritional advice</li>
      </ul>
    </div>
    <div class="back-body">
      <p class="invite">Book your free consultation today and take the first step toward achieving your goal! For detials contact me via ...</p>
      <ul class="contacts">
        <li><span class="contact-icon"><svg viewBox="0 0 10 10"><path d="M2 1.2 L3.6 1 L4.3 3 L3.3 3.8 Q4.2 5.8 6.2 6.7 L7 5.7 L9 6.4 L8.8 8 Q5.5 8.6 3 6.6 Q1 4.6 2 1.2Z" fill="#fff"/></svg></span>07700 918 342</li>
        <li><span class="contact-icon">@</span>calum@darbytraining.co.uk</li>
        <li><span class="contact-icon"></span>@calumdarbytraining</li>
        <li><span class="contact-icon"></span>calumdarbytraining</li>
      </ul>
    </div>
  </section>

  <section class="card card--back-slate" aria-label="Back, grey">
    <div class="back-header">
      <div class="back-header__brand">
        <p class="back-header__name"><span class="back-header__first">Calum Darby</span><span class="back-header__second">TRAINING</span></p>
        <span class="back-header__intro">Specializing in ...</span>
      </div>
      <ul class="services">
        <li>Weight loss &amp; tone</li>
        <li>Strength and conditioning</li>
        <li>Nutritional advice</li>
      </ul>
    </div>
    <div class="back-body">
      <p class="invite">Book your free consultation today and take the first step toward achieving your goal! For detials contact me via ...</p>
      <ul class="contacts">
        <li><span class="contact-icon"><svg viewBox="0 0 10 10"><path d="M2 1.2 L3.6 1 L4.3 3 L3.3 3.8 Q4.2 5.8 6.2 6.7 L7 5.7 L9 6.4 L8.8 8 Q5.5 8.6 3 6.6 Q1 4.6 2 1.2Z" fill="#fff"/></svg></span>07700 918 342</li>
        <li><span class="contact-icon">@</span>calum@darbytraining.co.uk</li>
        <li><span class="contact-icon"></span>@calumdarbytraining</li>
        <li><span class="contact-icon"></span>calumdarbytraining</li>
      </ul>
    </div>
  </section>
</body>
</html>
```